Australian small vineyard seeking wine label.

We need a wine label design for a new wine brand \Boutique winery - 2 vintages so far, looking for something a little eye catching, but simple.
Wine label name: Harlow and Co
2013 Cabernet Shiraz
2014 Shiraz
Estate grown
Vineyard located at Sevenhill in the Clare valley South Australia.

Target Market(s)

ladies aged between 20 and 50

Industry/Entity Type

Boutique

Logo Text

Harlow and Co

Logo styles of interest
Emblem Logo
Pictorial/Combination Logo
Abstract Logo
Character Logo
Font styles to use
Serif
Script

Requirements
Must have
• easy to read text
Nice to have
• The grape grower and winemaker is Martin Harlow -
• had some thoughts of Captain Brindle - Australian - naval flag
• But very open to ideas
Should not have
• over complications and colors due to cost of wine label being determined by amount of colors required abd print set up.

```html
<!DOCTYPE html>
<html lang="en">
<head>
<meta charset="utf-8">
<title>Harlow and Co Shiraz – Wine Label</title>
<link href="https://fonts.googleapis.com/css2?family=Cormorant+Garamond:wght@500;600&display=swap" rel="stylesheet">
<style>
  :root {
    --page-bg: #eeeeef;
    --label-cream: #efe6cf;
    --label-cream-deep: #e4d8b8;
    --wine-red: #8e1a22;
    --wine-red-dark: #6e1117;
    --ink: #1d1414;
    --brown-ink: #4a2a22;
    --name-white: #f6f1ea;
  }
  html, body {
    margin: 0;
    padding: 0;
    width: 1200px;
    height: 960px;
    overflow: hidden;
    background: var(--page-bg);
  }
  .canvas {
    position: relative;
    width: 1200px;
    height: 960px;
  }
  .wine-label {
    position: absolute;
    left: 310px;
    top: 45px;
    width: 580px;
    height: 870px;
    background: linear-gradient(90deg, var(--label-cream-deep) 0%, var(--label-cream) 18%, var(--label-cream) 82%, var(--label-cream-deep) 100%);
    box-shadow: 0 10px 30px rgba(0,0,0,0.12);
    overflow: hidden;
  }
  .label-bands {
    position: absolute;
    inset: 0 0 auto 0;
    width: 580px;
    height: 330px;
    display: block;
  }
  .brand-name {
    position: absolute;
    top: 72px;
    left: 0;
    right: 0;
    margin: 0;
    text-align: center;
    font-family: "Cormorant Garamond", serif;
    font-weight: 500;
    font-size: 72px;
    line-height: 1;
    letter-spacing: 1px;
    color: var(--name-white);
  }
  .ship-illustration {
    position: absolute;
    left: 145px;
    top: 345px;
    width: 290px;
    height: 250px;
    border-radius: 6px;
    background: radial-gradient(ellipse at 50% 50%, #c9b698 0%, #dccdaf 55%, rgba(239,230,207,0) 78%);
  }
  .wine-details {
    position: absolute;
    left: 0;
    right: 0;
    top: 635px;
    text-align: center;
    font-family: "Cormorant Garamond", serif;
    color: var(--brown-ink);
  }
  .variety {
    margin: 0;
    font-size: 44px;
    font-weight: 600;
    letter-spacing: 7px;
    line-height: 1;
  }
  .vintage {
    margin: 22px 0 0;
    font-size: 22px;
    font-weight: 500;
    letter-spacing: 1px;
  }
  .estate {
    margin: 10px 0 0;
    font-size: 19px;
    font-weight: 500;
    letter-spacing: 1.5px;
    font-variant: small-caps;
  }
  .region {
    margin: 34px 0 0;
    font-size: 16px;
    font-weight: 500;
    letter-spacing: 1.5px;
    font-variant: small-caps;
  }
</style>
</head>
<body>
  <main class="canvas">
    <section class="wine-label">
      <svg class="label-bands" viewBox="0 0 580 330" aria-hidden="true">
        <defs>
          <linearGradient id="redBand" x1="0" y1="0" x2="0" y2="1">
            <stop offset="0" stop-color="#6e1117"/>
            <stop offset="0.5" stop-color="#8e1a22"/>
            <stop offset="1" stop-color="#6e1117"/>
          </linearGradient>
        </defs>
        <path d="M0 0 H580 V205 C470 190 350 185 250 200 C160 214 80 222 0 212 Z" fill="url(#redBand)"/>
        <path d="M0 230 C90 240 170 232 260 218 C360 204 470 208 580 222 V246 C470 232 360 230 262 244 C170 258 90 262 0 254 Z" fill="#1d1414"/>
        <path d="M0 270 C90 278 170 272 262 258 C360 244 470 246 580 260" fill="none" stroke="#1d1414" stroke-width="3"/>
        <path d="M0 282 C90 290 170 284 262 270 C360 256 470 258 580 272" fill="none" stroke="#1d1414" stroke-width="1.5"/>
      </svg>

      <h1 class="brand-name">Harlow and Co</h1>

      <div class="ship-illustration" role="img" aria-label="Engraved sketch of a three-masted sailing ship under full sail"></div>

      <div class="wine-details">
        <p class="variety">SHIRAZ</p>
        <p class="vintage">2014</p>
        <p class="estate">Estate Grown</p>
        <p class="region">Millbrook&nbsp; Tarran Valley South Australia</p>
      </div>
    </section>
  </main>
</body>
</html>
```